Fahrzeugbeschriftung
Zielgruppe
Wir sind ein Bauingenieurbüro im Strassen- und Tiefbau sowie der Bauherrenberatung / Unterstützung. Unsere Zielgruppe sind primär öffentliche Institutionen (Städte, Gemeinden, Werke) welche Ihr Strassennetz sanieren möchten oder Werkleitungen erneuern. Wir planen das Bauvorhaben und machen anschliessend die Bauleitung. (Wir sind keine Bauunternehmung welche die Arbeiten baut)
Aufgabenstellung
Fahrzeug: VORNA 300 ELECTRIC 87 KW PRIMO, schwarz (schwarze Felgen)
Beschriftung: weiss
Das Design soll mit unserem Logo sein. Wichtig ist, dass es in weiss gehalten wird, da wir die Beschriftung mit dem Schneidplotter auf weises Folie möchten. Es ist keine Bedruckte Folie vorgesehen.
Wir möchten keine Standardbeschriftung sondern etwas was ein Hingucker ist.

```html
<!DOCTYPE html>
<html lang="de">
<head>
<meta charset="utf-8">
<title>KORVAL Bauingenieure AG – Fahrzeugbeschriftung</title>
<link href="https://fonts.googleapis.com/css2?family=Montserrat:wght@400;600&display=swap" rel="stylesheet">
<style>
  :root {
    --body-black: #0b0b0b;
    --foil-white: #f4f3ef;
  }
  html, body {
    margin: 0;
    padding: 0;
    overflow: hidden;
  }
  body {
    width: 1200px;
    height: 792px;
    background: var(--body-black);
    font-family: "Montserrat", Arial, sans-serif;
  }
  .wrap-panel {
    position: relative;
    width: 1200px;
    height: 792px;
    overflow: hidden;
  }
  .wrap-panel svg {
    position: absolute;
    inset: 0;
  }
  .swoosh {
    fill: var(--foil-white);
  }
  .rocker-stripe {
    fill: var(--foil-white);
  }
  .brand {
    position: absolute;
    left: 330px;
    top: 352px;
    color: var(--foil-white);
  }
  .brand-name {
    margin: 0;
    font-size: 58px;
    font-weight: 400;
    letter-spacing: 6px;
    line-height: 1;
  }
  .brand-tagline {
    margin: 12px 0 0 2px;
    font-size: 17px;
    font-weight: 400;
    letter-spacing: 5.4px;
    line-height: 1;
  }
  .web-address {
    position: absolute;
    left: 780px;
    top: 552px;
    margin: 0;
    font-size: 48px;
    font-weight: 600;
    line-height: 1;
    color: var(--body-black);
    transform: rotate(-24deg);
    transform-origin: left bottom;
    white-space: nowrap;
  }
</style>
</head>
<body>
  <main class="wrap-panel">
    <svg viewBox="0 0 1200 792" width="1200" height="792" aria-hidden="true">
      <path class="swoosh" d="M0,700 C420,660 860,500 1200,190 L1200,430 C1010,480 880,590 810,720 L0,720 Z"/>
      <rect class="rocker-stripe" x="0" y="720" width="810" height="24"/>
    </svg>
    <div class="brand">
      <p class="brand-name">KORVAL</p>
      <p class="brand-tagline">BAUINGENIEURE AG</p>
    </div>
    <p class="web-address">korval.ch</p>
  </main>
</body>
</html>
```